BRSP Business Card Design Project

We are a Wedding Film company in Charleston, SC In need of a unique business card. Our website is www.brightspiralreels.example. Check us out to get an idea of who we are and what we do. The design should be upscale but not pretentious. Modern but not cheesy. I will most likely have our cards printed by Zib on the Opal design. I'm also liking the raised designs for our logo. The Wedding Films in our logo on our site is blue so feel free to manipulate our logo for your designs as well.

Industry/Entity Type

Business

Requirements
Must have
• This is the info I want on the card:

Derek Hollisbury
Storyteller

Brightspiral Wedding Reels
www.brightspiralreels.example

555.208.4417
derek@brightspiralreels.example

```html
<!DOCTYPE html>
<html lang="en">
<head>
<meta charset="utf-8">
<title>Brightspiral Wedding Reels — Business Card</title>
<link rel="stylesheet" href="https://fonts.googleapis.com/css2?family=Open+Sans:wght@400;600;700&display=swap">
<style>
  :root {
    --backdrop: #efe9df;
    --gold-deep: #8d7748;
    --gold: #a88f5c;
    --gold-light: #d9cc98;
    --card-white: #ffffff;
    --ink-gold: #8a7650;
    --ink-muted: #7d6d4f;
    --shadow: rgba(60, 45, 20, 0.28);
  }
  * { box-sizing: border-box; margin: 0; padding: 0; }
  html, body { width: 1200px; height: 665px; overflow: hidden; }
  body {
    background: var(--backdrop);
    font-family: "Open Sans", Arial, sans-serif;
    position: relative;
  }
  .card {
    position: absolute;
    top: 190px;
    width: 500px;
    height: 286px;
    border-radius: 24px;
    overflow: hidden;
    box-shadow: 0 10px 24px var(--shadow);
  }
  .card--front { left: 70px; background: var(--card-white); }
  .card--back {
    left: 630px;
    background: radial-gradient(ellipse at 42% 38%, var(--gold-light) 0%, var(--gold) 45%, var(--gold-deep) 100%);
  }
  .front-band { position: absolute; inset: 0; width: 500px; height: 286px; }
  .holder {
    position: absolute; top: 20px; right: 26px; text-align: right; color: var(--card-white);
  }
  .holder__name { font-weight: 700; font-size: 16px; letter-spacing: 0.2px; }
  .holder__title { font-size: 11px; margin-top: 1px; }
  .brand {
    position: absolute; left: 34px; top: 128px;
    display: flex; align-items: center; gap: 12px;
  }
  .brand__dot {
    width: 22px; height: 22px; border-radius: 50%; background: var(--ink-gold); flex: none;
  }
  .brand__name {
    color: var(--ink-gold); font-weight: 400; font-size: 24px; line-height: 1.15;
  }
  .contact {
    position: absolute; right: 26px; top: 170px; text-align: right;
    color: var(--ink-muted); font-size: 12px; line-height: 22px;
  }
  .contact__row { display: flex; justify-content: flex-end; align-items: center; gap: 7px; }
  .contact svg { width: 12px; height: 12px; flex: none; }
  .website {
    position: absolute; left: 34px; bottom: 22px;
    display: flex; align-items: center; gap: 7px;
    color: var(--ink-muted); font-size: 12px;
  }
  .website svg { width: 11px; height: 11px; }
  .back-mark {
    position: absolute; inset: 0; display: flex; flex-direction: column;
    align-items: center; justify-content: center; gap: 14px;
  }
  .back-mark__dot { width: 34px; height: 34px; border-radius: 50%; background: var(--card-white); }
  .back-mark__name {
    color: var(--card-white); font-weight: 600; font-size: 26px; text-align: center; line-height: 1.2;
  }
</style>
</head>
<body>
  <section class="card card--front" aria-label="Business card front">
    <svg class="front-band" viewBox="0 0 500 286" aria-hidden="true">
      <defs>
        <radialGradient id="bandGold" cx="0.55" cy="0.2" r="0.7">
          <stop offset="0" stop-color="#d9cc98"/>
          <stop offset="0.5" stop-color="#a88f5c"/>
          <stop offset="1" stop-color="#8d7748"/>
        </radialGradient>
      </defs>
      <path d="M0 0 H500 V62 C360 40 200 48 60 92 C30 102 10 110 0 116 Z" fill="url(#bandGold)"/>
      <path d="M0 124 C20 112 60 98 110 86 C250 56 380 54 500 74 V80 C380 62 250 66 120 94 C70 104 30 116 0 130 Z" fill="url(#bandGold)"/>
    </svg>

    <div class="holder">
      <div class="holder__name">Derek Hollisbury</div>
      <div class="holder__title">Storyteller</div>
    </div>

    <div class="brand">
      <span class="brand__dot"></span>
      <span class="brand__name">Brightspiral<br>Wedding Reels</span>
    </div>

    <div class="contact">
      <div class="contact__row">555.208.4417
        <svg viewBox="0 0 12 12" aria-hidden="true"><circle cx="6" cy="6" r="5.3" fill="none" stroke="currentColor" stroke-width="0.9"/><path d="M4 3.2 L5 3 5.4 4.6 4.8 5.1 Q5.4 6.5 6.9 7.2 L7.4 6.6 9 7 8.8 8 Q6 8.6 3.8 5.3 Z" fill="currentColor"/></svg>
      </div>
      <div class="contact__row">derek@brightspiralreels.example
        <svg viewBox="0 0 12 12" aria-hidden="true"><rect x="1" y="3" width="10" height="6.5" fill="currentColor"/><path d="M1 3 L6 7 11 3" fill="none" stroke="#fff" stroke-width="0.8"/></svg>
      </div>
    </div>

    <div class="website">
      <svg viewBox="0 0 12 12" aria-hidden="true"><circle cx="6" cy="6" r="5" fill="none" stroke="currentColor" stroke-width="1"/><circle cx="6" cy="6" r="2.2" fill="currentColor"/></svg>
      www.brightspiralreels.example
    </div>
  </section>

  <section class="card card--back" aria-label="Business card back">
    <div class="back-mark">
      <span class="back-mark__dot"></span>
      <span class="back-mark__name">Brightspiral<br>Wedding Reels</span>
    </div>
  </section>
</body>
</html>
```